Cosmetic Clinic Looking For Sign Designs

We are looking for sign design ideas for the front of our building and a lawn sign for our cosmetic injection salon.
I have uploaded the front of our building for a mock up and size, lawn posts with size and a sign that uses the same dimensions.
We would like both signs to be black for the background.

Target Market(s)

Ages 18-75

Industry/Entity Type

Beauty

Requirements
Must have
• Services we offer:
• Cosmetic Injections
• Airbrush Spray Tanning
• Eyelash Growth Serum
• Skin Care Products & More
• Everything must be on a black background
• The lawn sign must have the address: 394 Fenwick and the building sign should have the phone number.
Should not have
• Nothing can light up (no LED)
• Both signs do not need the full address. Just 394 Fenwick and the phone number

```html
<!DOCTYPE html>
<html lang="en">
<head>
<meta charset="utf-8">
<title>Let's Shine Studio – Sign</title>
<link rel="stylesheet" href="https://fonts.googleapis.com/css2?family=Arimo:wght@700&display=swap">
<style>
  :root {
    --page: #ffffff;
    --sign-black: #000000;
    --accent-pink: #e8186f;
    --brand-teal: #2196b0;
    --marker-lavender: #7b80c0;
    --text-white: #ffffff;
    --photo-skin: #d9a88a;
    --photo-dark: #2a2a30;
    --photo-light: #ece6e2;
  }
  * { margin: 0; padding: 0; box-sizing: border-box; }
  html, body { width: 1200px; height: 1200px; overflow: hidden; background: var(--page); }
  .canvas { position: relative; width: 1200px; height: 1200px; }
  .sign-shape { position: absolute; inset: 0; width: 1200px; height: 1200px; }
  .sign-content { position: absolute; inset: 0; text-align: center; }
  .studio-name {
    position: absolute; left: 340px; width: 520px; top: 398px;
    font-family: "Arimo", Arial, sans-serif; font-weight: 700;
    font-size: 62px; line-height: 68px; color: var(--brand-teal);
    text-align: center;
  }
  .services-heading {
    position: absolute; left: 0; width: 1200px; top: 550px;
    font-family: "Arimo", Arial, sans-serif; font-weight: 700; font-size: 37px;
    line-height: 40px; color: var(--accent-pink);
  }
  .services-list {
    position: absolute; left: 0; width: 1200px; top: 596px; list-style: none;
    font-family: "Arimo", Arial, sans-serif; font-weight: 700; font-size: 23px;
    line-height: 29.5px; color: var(--text-white);
  }
  .divider { position: absolute; left: 358px; width: 498px; height: 2px; background: var(--accent-pink); }
  .divider.top { top: 739px; }
  .divider.bottom { top: 887px; }
  .gallery { position: absolute; top: 752px; left: 382px; display: flex; gap: 22px; }
  .gallery .photo {
    width: 132px; height: 119px; border: 3px solid var(--accent-pink); border-radius: 9px;
  }
  .photo.brow-makeup { background: linear-gradient(135deg, #e2b49a, var(--photo-skin) 60%, #b98468); }
  .photo.glam-portrait { background: radial-gradient(circle at 65% 40%, #6b5a52, var(--photo-dark) 65%); }
  .photo.skin-portrait { background: linear-gradient(120deg, #e8c2ac, var(--photo-light) 70%); }
  .address {
    position: absolute; left: 0; width: 1200px; top: 901px;
    font-family: "Arimo", Arial, sans-serif; font-weight: 700; font-size: 31px;
    line-height: 36px; color: var(--text-white);
  }
  .phone {
    position: absolute; left: 0; width: 1200px; top: 948px;
    font-family: "Arimo", Arial, sans-serif; font-weight: 700; font-size: 52px;
    line-height: 56px; color: var(--text-white);
  }
</style>
</head>
<body>
<main class="canvas">
  <svg class="sign-shape" viewBox="0 0 1200 1200" aria-hidden="true">
    <path class="sign-board" fill="var(--sign-black)"
      d="M305,1034 V362 C305,325 340,302 377,292 C388,245 415,217 445,217 C465,217 478,222 489,238 C525,195 565,173 603,173 C641,173 681,195 717,238 C728,222 741,217 761,217 C791,217 818,245 829,292 C866,302 901,325 901,362 V1034 Z"/>
    <path class="sign-border" fill="none" stroke="var(--accent-pink)" stroke-width="2" vector-effect="non-scaling-stroke"
      transform="translate(603 603.5) scale(0.968 0.975) translate(-603 -603.5)"
      d="M305,1034 V362 C305,325 340,302 377,292 C388,245 415,217 445,217 C465,217 478,222 489,238 C525,195 565,173 603,173 C641,173 681,195 717,238 C728,222 741,217 761,217 C791,217 818,245 829,292 C866,302 901,325 901,362 V1034 Z"/>
    <circle class="top-marker" cx="604" cy="295" r="70" fill="var(--marker-lavender)"/>
  </svg>

  <section class="sign-content">
    <h1 class="studio-name">LET’S SHINE STUDIO</h1>

    <h2 class="services-heading">Services we offer:</h2>
    <ul class="services-list">
      <li>Cosmetic Injections</li>
      <li>Airbrush Spray Tanning</li>
      <li>Eyelash Growth Serum</li>
      <li>Skin Care Products &amp; More</li>
    </ul>

    <div class="divider top"></div>
    <div class="gallery">
      <div class="photo brow-makeup" role="img" aria-label="Close-up photo of eyebrow makeup being applied with a brush"></div>
      <div class="photo glam-portrait" role="img" aria-label="Photo of a woman with curly hair and evening makeup"></div>
      <div class="photo skin-portrait" role="img" aria-label="Photo of a woman with clear skin beside white flowers"></div>
    </div>
    <div class="divider bottom"></div>

    <p class="address">394 Fenwick and the building</p>
    <p class="phone">000 0000 000</p>
  </section>
</main>
</body>
</html>
```